TalkBridge - Language Coaching Services

Sleek, innovative, trendy design for Language Coaching business.

TalkBridge is a new UK based company that provides Language Coaching services. We offer highly personalized on-line and face to face language courses. We also impart learning techniques workshops based on the latest neuroscience research for second-language acquisition.

Target Market(s)

Industry/Entity Type

Consulting

Contact Information for Business Card

TalkBridge
ElenaVT@talkbridge-demo.co.uk
TalkBridge-demo.co.uk
London, UK

Font styles to use
Sans Serif

```html
<!DOCTYPE html>
<html lang="en">
<head>
<meta charset="utf-8">
<title>TalkBridge Business Card</title>
<link href="https://fonts.googleapis.com/css2?family=Lato:wght@300;400;700;900&display=swap" rel="stylesheet">
<style>
  :root {
    --stage: #2b2b2d;
    --teal-light: #2aa3cc;
    --teal-dark: #19699a;
    --brand: #1f8fbf;
    --ink: #333a40;
    --paper: #fbfcfd;
    --faint: rgba(255,255,255,0.14);
    --faint-blue: rgba(31,143,191,0.10);
  }
  * { margin: 0; padding: 0; box-sizing: border-box; }
  html, body { width: 1200px; height: 900px; overflow: hidden; }
  body {
    background: var(--stage);
    font-family: 'Lato', sans-serif;
    position: relative;
  }
  .card {
    position: absolute;
    width: 700px;
    height: 400px;
    overflow: hidden;
    box-shadow: 0 12px 30px rgba(0,0,0,0.45);
  }
  .card-front {
    left: 150px; top: 30px;
    background: linear-gradient(150deg, var(--teal-light) 0%, var(--teal-dark) 100%);
  }
  .front-ring {
    position: absolute; left: 250px; top: 60px;
    width: 230px; height: 230px; border-radius: 50%;
    border: 22px solid var(--faint);
  }
  .front-wordmark {
    position: absolute; left: 0; right: 0; top: 140px;
    text-align: center; color: #fff;
    font-size: 62px; font-weight: 400; letter-spacing: 3px;
  }
  .front-url {
    position: absolute; left: 0; right: 0; top: 300px;
    text-align: center; color: #fff;
    font-size: 17px; font-weight: 400; letter-spacing: 7px;
  }
  .card-back {
    left: 350px; top: 470px;
    background: var(--paper);
  }
  .back-ring {
    position: absolute; right: -40px; top: 10px;
    width: 300px; height: 300px; border-radius: 50%;
    border: 26px solid var(--faint-blue);
  }
  .logo {
    position: absolute; left: 150px; top: 60px; width: 300px;
    text-align: center;
  }
  .logo-dot {
    display: block; margin: 0 auto 12px;
    width: 84px; height: 84px; border-radius: 50%;
    border: 6px solid var(--brand);
  }
  .logo-name {
    color: var(--brand); font-size: 46px; font-weight: 400; letter-spacing: 2px;
  }
  .person {
    position: absolute; right: 40px; top: 150px; text-align: right;
  }
  .person-name { color: var(--brand); font-size: 21px; }
  .person-name .first { font-weight: 300; }
  .person-name .last { font-weight: 700; }
  .person-title { color: var(--ink); font-size: 15px; margin-top: 2px; }
  .contact {
    position: absolute; left: 40px; top: 232px; list-style: none;
    color: var(--ink); font-size: 16px;
  }
  .contact li { display: flex; align-items: center; height: 26px; }
  .contact svg { width: 16px; height: 16px; margin-right: 12px; fill: var(--brand); }
  .band {
    position: absolute; left: 0; right: 0; bottom: 0; height: 62px;
    background: linear-gradient(90deg, var(--teal-light), var(--teal-dark));
    color: #fff; font-weight: 700; font-size: 17px;
    display: flex; align-items: center; justify-content: center;
  }
</style>
</head>
<body>
  <section class="card card-front">
    <div class="front-ring"></div>
    <div class="front-wordmark">TALKBRIDGE</div>
    <div class="front-url">www.TalkBridge-demo.co.uk</div>
  </section>

  <section class="card card-back">
    <div class="back-ring"></div>
    <div class="logo">
      <span class="logo-dot"></span>
      <div class="logo-name">TALKBRIDGE</div>
    </div>
    <div class="person">
      <div class="person-name"><span class="first">Maya</span> <span class="last">Holloway</span></div>
      <div class="person-title">Chief Executive Offer</div>
    </div>
    <ul class="contact">
      <li><svg viewBox="0 0 16 16"><path d="M3 1h3l1 4-2 1c1 2 3 4 5 5l1-2 4 1v3c0 1-1 2-2 2C7 15 1 9 1 3c0-1 1-2 2-2z"/></svg>020.7946.0321</li>
      <li><svg viewBox="0 0 16 16"><rect x="4" y="1" width="8" height="4"/><rect x="1" y="6" width="14" height="6" rx="1"/><rect x="4" y="10" width="8" height="5"/></svg>020.7946.0874</li>
      <li><svg viewBox="0 0 16 16"><path d="M1 3h14v10H1z M1 3l7 6 7-6" stroke="#fff" stroke-width="1"/></svg>ElenaVT@talkbridge-demo.co.uk</li>
    </ul>
    <div class="band">14 Harbour Row, Suite 3, London EC1A 4BX</div>
  </section>
</body>
</html>
```